Bussines Card - TR EDIFICACIONES, S.A.

We need a design for a business card.
I want it to look professional, but not old fashion.
We are like "young people', somehow i want it to look fresh, new, different, but still serious and professional.
I could use, a non typical design. (I mean, not just rectangular design).

The company Name is " TR EDIFICACIONES, S.A. " we are Panamenian company (spanish language) dedicated to construction and civil engeniering.

The company logo is attached, i use it with white background. Im not sure trying different one, could try.

Industry/Entity Type

Business

```html
<!DOCTYPE html>
<html lang="es">
<head>
<meta charset="utf-8">
<title>TR Edificaciones – Tarjeta de presentación</title>
<link href="https://fonts.googleapis.com/css2?family=Archivo:wght@700&family=Fira+Sans+Condensed:wght@600&family=PT+Sans&display=swap" rel="stylesheet">
<style>
  :root {
    --stage-light: #ececed;
    --stage-dark: #c3c4c6;
    --card-dark: #58585a;
    --grad-start: #5d5e60;
    --grad-mid: #a4a7aa;
    --grad-end: #eef2f4;
    --ink: #111111;
    --white: #ffffff;
    --accent: #b3141c;
  }
  * { margin: 0; padding: 0; box-sizing: border-box; }
  html, body { width: 1200px; height: 1200px; overflow: hidden; }
  body {
    position: relative;
    background: radial-gradient(circle at 50% 50%, var(--stage-light) 0%, var(--stage-light) 35%, var(--stage-dark) 100%);
  }
  .card {
    position: absolute;
    left: 228px;
    width: 742px;
    height: 422px;
    overflow: hidden;
  }
  .card--front {
    top: 167px;
    border-radius: 36px 0 36px 0;
    background: linear-gradient(90deg, var(--grad-start) 0%, var(--grad-mid) 55%, var(--grad-end) 100%);
  }
  .card--back {
    top: 600px;
    border-radius: 0 36px 0 36px;
    background: var(--card-dark);
  }
  .holder { position: absolute; left: 56px; top: 91px; color: var(--ink); font-family: "Archivo", Arial, sans-serif; }
  .holder__name { font-size: 24px; font-weight: 700; line-height: 1.1; }
  .holder__role { font-size: 20px; font-weight: 700; line-height: 1.3; }
  .brand-mark {
    position: absolute; left: 506px; top: 19px;
    width: 141px; height: 139px;
    background: var(--card-dark);
  }
  .brand-name {
    position: absolute; right: 22px; top: 188px;
    font-family: "Fira Sans Condensed", Arial, sans-serif;
    font-weight: 600; font-size: 26px; letter-spacing: 3.2px;
    color: var(--card-dark);
  }
  .contact {
    position: absolute; left: 38px; top: 259px;
    list-style: none;
    font-family: "PT Sans", Arial, sans-serif;
    font-size: 20px; color: var(--white); line-height: 24px;
  }
  .contact__item { display: flex; align-items: flex-start; margin-bottom: 4px; }
  .contact__item--address { margin-bottom: 8px; }
  .contact__icon { width: 18px; height: 18px; margin: 3px 8px 0 0; flex: none; }
  .back-name {
    position: absolute; right: 62px; bottom: 56px;
    text-align: right;
    font-family: "Fira Sans Condensed", Arial, sans-serif;
    font-weight: 600; font-size: 58px; line-height: 1.05; letter-spacing: 4px;
    color: var(--white);
  }
</style>
</head>
<body>
  <section class="card card--front">
    <div class="holder">
      <p class="holder__name">YOUR NAME</p>
      <p class="holder__role">Position</p>
    </div>
    <div class="brand-mark"></div>
    <p class="brand-name">TR EDIFICACIONES</p>
    <ul class="contact">
      <li class="contact__item contact__item--address">
        <svg class="contact__icon" viewBox="0 0 18 18" aria-hidden="true"><circle cx="9" cy="9" r="9" fill="var(--accent)"/><path d="M4 9 9 4.5 14 9h-1.6v4.5H5.6V9z" fill="#fff"/><rect x="8" y="10.5" width="2" height="3" fill="var(--accent)"/></svg>
        <span>Calle 48, Bella Vista,<br>Torre Marela, 2do Piso Local 4</span>
      </li>
      <li class="contact__item">
        <svg class="contact__icon" viewBox="0 0 18 18" aria-hidden="true"><circle cx="9" cy="9" r="9" fill="var(--accent)"/><path d="M5 6.5c0-1 1-1.8 2-1.8l1 2.2-1 .9c.5 1.2 1.4 2.1 2.6 2.6l.9-1 2.2 1c0 1-.8 2-1.8 2C7.8 12.4 5 9.6 5 6.5z" fill="#fff"/></svg>
        <span>287-5163</span>
      </li>
      <li class="contact__item">
        <svg class="contact__icon" viewBox="0 0 18 18" aria-hidden="true"><circle cx="9" cy="9" r="9" fill="var(--accent)"/><rect x="6" y="3.5" width="6" height="11" rx="1" fill="#fff"/><rect x="7" y="5" width="4" height="5" fill="var(--accent)"/></svg>
        <span>555-555-5555</span>
      </li>
      <li class="contact__item">
        <svg class="contact__icon" viewBox="0 0 18 18" aria-hidden="true"><circle cx="9" cy="9" r="9" fill="var(--accent)"/><rect x="4" y="5.5" width="10" height="7" fill="#fff"/><path d="M4 5.5 9 9.5l5-4" fill="none" stroke="var(--accent)" stroke-width="1.2"/></svg>
        <span>your email address</span>
      </li>
    </ul>
  </section>

  <section class="card card--back">
    <p class="back-name">TR<br>EDIFICACIONES</p>
  </section>
</body>
</html>
```